Ridgeline Build Network Inc. Letterhead

Creation of attractive and eye catching letterhead for a business start-up for the construction industry. Letterhead must relate to construction, but avoid standard hammer and tools in the design.
Updates

I forgot to add some details, sorry about that. Some pertinent info: Ph: 916-555-0148 ridgelinebuildnet.example 487 Willowmere Ave, Ste 210 Folsom, CA 95699 info@ridgelinebuildnet.example not sure if slogan should be in there" “Connecting construction professionals to create a purpose driven industry.” must be able to be used in word. Thanks!

```html
<!DOCTYPE html>
<html lang="en">
<head>
<meta charset="utf-8">
<title>Ridgeline Build Network Inc. Letterhead</title>
<link rel="stylesheet" href="https://fonts.googleapis.com/css2?family=Open+Sans:wght@400;600;700&display=swap">
<style>
  :root {
    --backdrop: #d2d2d2;
    --paper: #ffffff;
    --navy: #101a45;
    --red: #c0202e;
    --ink: #3a3a3a;
    --muted: #777b86;
    --faint: #f1ecec;
  }
  * { box-sizing: border-box; margin: 0; padding: 0; }
  html, body {
    width: 1200px; height: 795px; overflow: hidden;
    background: var(--backdrop);
    font-family: "Open Sans", Arial, sans-serif;
  }
  .letterhead {
    position: absolute; left: 338px; top: 28px;
    width: 524px; height: 740px;
    background: var(--paper);
    box-shadow: 0 6px 18px rgba(0,0,0,0.18);
    overflow: hidden;
    color: var(--ink);
  }
  .brand {
    position: absolute; left: 40px; top: 44px;
    display: flex; align-items: center; gap: 7px;
    font-size: 13px; font-weight: 700; color: var(--navy);
    letter-spacing: 0.2px;
  }
  .brand-mark { width: 10px; height: 10px; background: var(--red); }
  .contact {
    position: absolute; right: 40px; top: 40px;
    list-style: none; font-size: 8px; line-height: 13px; color: var(--ink);
  }
  .contact li { display: flex; align-items: center; gap: 5px; }
  .contact svg { width: 8px; height: 8px; fill: var(--red); flex: none; }
  .letter {
    position: absolute; left: 40px; top: 130px; width: 420px;
    font-size: 8.5px; line-height: 12px;
  }
  .date { margin-bottom: 14px; font-weight: 600; font-size: 9px; }
  .recipient { font-weight: 600; font-size: 9px; line-height: 12px; margin-bottom: 14px; }
  .salutation { font-weight: 700; font-size: 10px; margin-bottom: 12px; }
  .body-text p { margin-bottom: 11px; color: var(--muted); }
  .closing {
    position: absolute; right: 60px; top: 408px;
    font-size: 8.5px; color: var(--ink);
  }
  .closing .sign-line { display: block; margin-top: 18px; width: 70px; border-top: 1px solid var(--ink); }
  .faint-name {
    position: absolute; right: 40px; top: 470px;
    font-size: 22px; font-weight: 700; color: var(--faint);
  }
  .footer-wave { position: absolute; left: 0; bottom: 0; width: 524px; height: 260px; display: block; }
  .footer-info {
    position: absolute; left: 40px; bottom: 24px; color: #fff;
    font-size: 10px; line-height: 14px;
  }
  .footer-info strong { font-weight: 700; font-size: 11px; display: block; }
</style>
</head>
<body>
  <article class="letterhead">
    <div class="brand"><span class="brand-mark"></span>Ridgeline Build Network Inc.</div>

    <ul class="contact">
      <li><svg viewBox="0 0 10 10"><path d="M2 0h2l1 3-1.5 1a6 6 0 0 0 2.5 2.5L7 5l3 1v2a2 2 0 0 1-2 2A8 8 0 0 1 0 2a2 2 0 0 1 2-2z"/></svg>916-555-0148</li>
      <li><svg viewBox="0 0 10 10"><path d="M0 2h10v6H0z M0 2l5 3.5L10 2" stroke="#fff" stroke-width="0.8"/></svg>info@ridgelinebuildnet.example</li>
      <li><svg viewBox="0 0 10 10"><circle cx="5" cy="5" r="5"/></svg>www.ridgelinebuildnet.example</li>
    </ul>

    <section class="letter">
      <p class="date">January 12, 2014</p>
      <p class="recipient">Mr. John Doe<br>President<br>AA Corporation<br>111 Street Name, Suite#<br>City, State, 12345</p>
      <p class="salutation">Dear Mr. John,</p>
      <div class="body-text">
        <p>Lorem Ipsum is simply dummy text of the printing and typesetting industry. Lorem Ipsum has been the industry's standard dummy text ever since the 1500s, when an unknown printer took a galley of type and scrambled it to make a type specimen book. It has survived not only five centuries, but also the leap into electronic typesetting, remaining essentially unchanged.</p>
        <p>The standard chunk of Lorem Ipsum used since the 1500s is reproduced below for those interested. Sections 1.10.32 and 1.10.33 from "de Finibus Bonorum et Malorum" by Cicero are also reproduced in their exact original form, accompanied by English versions from the 1914 translation by H. Rackham.</p>
        <p>Lorem Ipsum is simply dummy text of the printing and typesetting industry. Lorem Ipsum has been the industry's standard dummy text ever since the 1500s, when an unknown printer took a galley of type and scrambled it to make a type specimen book. It has survived not only five centuries, but also the leap into electronic typesetting, remaining essentially unchanged. It was popularised in the</p>
      </div>
    </section>

    <div class="closing">Sincerely Your,<span class="sign-line"></span></div>

    <div class="faint-name" aria-hidden="true">Ridgeline</div>

    <svg class="footer-wave" viewBox="0 0 524 260" preserveAspectRatio="none" aria-hidden="true">
      <path d="M0,118 C190,122 390,48 524,0" fill="none" stroke="#e4e4e8" stroke-width="3"/>
      <path d="M0,130 C190,135 390,60 524,10 L524,30 C390,80 190,152 0,152 Z" fill="var(--red)"/>
      <path d="M0,152 C190,152 390,80 524,30 L524,260 L0,260 Z" fill="var(--navy)"/>
      <path d="M0,152 C190,152 390,80 524,30" fill="none" stroke="#fff" stroke-width="1.5"/>
      <path d="M250,260 C360,190 450,110 524,72" fill="none" stroke="var(--red)" stroke-width="2.5"/>
    </svg>

    <div class="footer-info">
      <strong>Ridgeline Build Network Inc.</strong>
      487 Willowmere Ave, Ste 210, Folsom, CA 95699
    </div>
  </article>
</body>
</html>
```